Ghost Tour and Pub Crawl Rack Card Brochure

We are looking to get an updated design for our rack cards that are printed on 4x9 vertical cards. We have uploaded our logo and our previous design. We are looking for a new idea. We need something that jumps out at you when they are printed and sitting next to a group of 50 other brochures. It needs to have all of the must haves incorporated.

Target Market(s)

Women

Industry/Entity Type

Tourism

Font styles to use
Serif
Sans Serif
Decorative
Script
Other font styles liked:
• Doesn't Matter

Colors

Designer to choose colors to be used in the design.

Requirements
Must have
• Needs to be a design that jumps out at you when you are looking at 50 of these in a rack from all different companies.
• 1. Instead of it being just Ghost Tour Pub Crawl, we would like it to have some sort of design that is Ghost Tours and Pub Crawls.
• 2. Our Website must be prominent www.DuskLanternWalks.com
• 2. We want a box for text at the bottom that we can add a promo code ourselves to the design, so just something that we can edit later that allows us to have enough space to write a promo code, city name, and alternate phone number.
• 3. We want it to say save 10% instead of $5.00
• 4. Phone number 1-8-Moon-Walk listed on the card
Nice to have
• Needs to be Spooky, but stand out.

```html
<!DOCTYPE html>
<html lang="en">
<head>
<meta charset="utf-8">
<title>Ghost Tour Pub Crawl Rack Card</title>
<link href="https://fonts.googleapis.com/css2?family=Creepster&family=Rubik+Wet+Paint&display=swap" rel="stylesheet">
<style>
  :root {
    --stage: #707070;
    --card: #0b0b0a;
    --scene-light: #4a4634;
    --scene-mid: #2a2820;
    --scene-dark: #0b0b0a;
    --glow: rgba(240, 138, 18, 0.22);
    --pumpkin: #f08a12;
    --bone: #ffffff;
  }
  html, body {
    margin: 0;
    width: 1200px;
    height: 1200px;
    overflow: hidden;
    background: var(--stage);
  }
  .rack-card {
    position: absolute;
    left: 370px;
    top: 80px;
    width: 463px;
    height: 1040px;
    background: var(--card);
    overflow: hidden;
    text-align: center;
    color: var(--pumpkin);
    font-family: "Creepster", cursive;
  }
  .haunted-scene {
    position: absolute;
    inset: 0;
    background:
      radial-gradient(ellipse 55% 30% at 50% 62%, var(--glow) 0%, rgba(240,138,18,0) 100%),
      radial-gradient(ellipse 75% 50% at 50% 40%, var(--scene-light) 0%, var(--scene-mid) 45%, var(--scene-dark) 100%);
  }
  .headline {
    position: absolute;
    left: 0;
    width: 100%;
    margin: 0;
    font-weight: 400;
    line-height: 1;
  }
  .headline--ghost { top: 78px; font-size: 70px; letter-spacing: 4px; word-spacing: 10px; }
  .headline--pub { top: 150px; font-size: 44px; letter-spacing: 3px; word-spacing: 16px; }
  .brand-name {
    position: absolute;
    top: 336px;
    left: 0;
    width: 100%;
    font-size: 52px;
    line-height: 1;
    color: var(--bone);
  }
  .offer-amount {
    position: absolute;
    top: 452px;
    left: 0;
    width: 100%;
    font-size: 200px;
    line-height: 1;
    letter-spacing: 22px;
    text-indent: 22px;
  }
  .offer-label {
    position: absolute;
    top: 664px;
    left: 0;
    width: 100%;
    font-family: "Rubik Wet Paint", cursive;
    font-size: 70px;
    line-height: 1;
    color: var(--bone);
  }
  .promo-box {
    position: absolute;
    left: 22px;
    right: 22px;
    top: 796px;
    height: 214px;
    box-sizing: border-box;
    border: 3px dashed var(--pumpkin);
    border-radius: 10px;
    background: rgba(0, 0, 0, 0.55);
  }
  .details {
    margin: 0;
    padding: 12px 0 0;
    list-style: none;
    font-size: 27px;
    letter-spacing: 1px;
    text-transform: uppercase;
  }
  .details li { height: 46px; line-height: 46px; }
  .details .website {
    height: 54px;
    line-height: 54px;
    font-size: 33px;
    color: var(--bone);
  }
</style>
</head>
<body>
  <section class="rack-card">
    <div class="haunted-scene" role="img" aria-label="Haunted house silhouette with bare trees and flying bats in a dark night sky"></div>
    <h1 class="headline headline--ghost">Ghost Tour</h1>
    <h2 class="headline headline--pub">Pub Crawl</h2>
    <div class="brand-name">Dusk Lantern Walks</div>
    <div class="offer-amount">10%</div>
    <div class="offer-label">SAVE</div>
    <div class="promo-box">
      <ul class="details">
        <li>City Name: Lorem Ipsum</li>
        <li>Pomo Cord: 00000</li>
        <li class="website">www.DuskLanternWalks.com</li>
        <li>Call us: 1-8-Moon-Walk</li>
      </ul>
    </div>
  </section>
</body>
</html>
```